Brix2Key Header

I want a professional Letterhead for my law firm. I'm attaching the letterhead I currently use in Word and PDF form. I'm also attaching my logo, and an example header that I like.

```html
<!DOCTYPE html>
<html lang="en">
<head>
<meta charset="utf-8">
<title>Brix2Key Letterhead</title>
<link href="https://fonts.googleapis.com/css2?family=Tinos:wght@400;700&display=swap" rel="stylesheet">
<style>
  :root {
    --backdrop: #d9dcdd;
    --paper: #ffffff;
    --brand-blue: #2166b0;
    --brand-green: #4a7d43;
    --ink-dark: #333333;
    --ink-body: #3a3a3a;
  }
  * { margin: 0; padding: 0; box-sizing: border-box; }
  html, body {
    width: 1200px; height: 784px; overflow: hidden;
    background: var(--backdrop);
    font-family: "Tinos", "Times New Roman", serif;
  }
  .letterhead {
    position: absolute; left: 314px; top: 22px;
    width: 572px; height: 740px;
    background: var(--paper);
    box-shadow: 0 2px 6px rgba(0,0,0,0.12);
  }
  .header-rule { position: absolute; left: 0; right: 0; height: 4px; }
  .header-rule--blue { top: 8px; left: 14px; background: var(--brand-blue); }
  .header-rule--green { top: 15px; background: var(--brand-green); }
  .firm-name {
    position: absolute; left: 30px; top: 30px;
    font-weight: 700; font-size: 34px; letter-spacing: 1px;
    color: var(--ink-dark); text-transform: uppercase;
  }
  .contact-block {
    position: absolute; right: 18px; top: 44px;
    font-size: 9.5px; line-height: 13px; color: var(--ink-body);
    text-transform: uppercase;
  }
  .contact-block p { white-space: nowrap; }
  .contact-name { color: var(--brand-blue); font-weight: 700; }
  .contact-address { color: var(--brand-green); font-weight: 700; }
  .dot {
    display: inline-block; width: 7px; height: 7px; border-radius: 50%;
    background: var(--brand-green); margin: 0 3px 0 4px; vertical-align: -0.5px;
  }
  .dot:first-child { margin-left: 0; }
  .footer-rules { position: absolute; left: 0; bottom: 0; width: 572px; height: 40px; }
</style>
</head>
<body>
  <main class="letterhead">
    <div class="header-rule header-rule--blue"></div>
    <div class="header-rule header-rule--green"></div>

    <div class="firm-name">Brix2Key</div>

    <address class="contact-block" style="font-style:normal">
      <p class="contact-name">Dorian K. Vallez III, Attorney at Law, PLLC</p>
      <p class="contact-address"><span class="dot"></span>2480 Harwood Lane Suite 200 Dallas, Texas 75204</p>
      <p><span class="dot"></span>(877) 555-0142<span class="dot"></span>(469) 555-0187<span class="dot"></span>brix@brix2key.net</p>
      <p><span class="dot"></span>www.brix2key.com</p>
    </address>

    <svg class="footer-rules" viewBox="0 0 572 40" aria-hidden="true">
      <!-- thin line -->
      <rect x="0" y="14" width="150" height="3" fill="var(--brand-green)"/>
      <rect x="156" y="18" width="230" height="3" fill="var(--brand-blue)"/>
      <rect x="392" y="22" width="180" height="3" fill="var(--brand-green)"/>
      <!-- thick band -->
      <rect x="0" y="30" width="420" height="10" fill="var(--brand-green)"/>
      <rect x="420" y="30" width="152" height="10" fill="var(--brand-blue)"/>
    </svg>
  </main>
</body>
</html>
```